New Business Card Design Project

We need to enhance the look and feel of our brand. We are starting with the business card and will hopefully expand to letter head, website, etc. The firm is based in Kolding Denmark and invests with global pension funds and for mutual fund investors alike. We would like to see an innovative use of the companies logo (star on the website - www.northmerrowcap.com) and a broader use of a color palette. Presently it is dominantly shades of blue. The firm wants to convey a sense they are a creative investment team that understands all the risks in the emerging markets and have the skills to perform in an environment of uncertainty.

Presently, we have three locations: Kolding Denmark, Glendale CA USA, Zurich Switzerland. We also have a prominently displayed bar code square on a solid dark blue back that will take smart phone users to the firm's website. I am indifferent to its inclusion., Details for my new Business Card Design Project will be added soon.
Updates

Project Deadline Extended
Reason: Designers, I am working with on getting feedback from both US and Danish partners on preferences. That is taking slightly more time than expected. Thanks for you patience. Nice work. TLV

Target Market(s)

The target market is a combination of institutional and retail investors. The european arm uses a card similar to a couple of those submitted.

Industry/Entity Type

Environment

Requirements
Must have
• The company's Star Logo. See www.northmerrowcap.com. It may be used in its current form or some new clever way. The founders are Danish and have a strong affinity for it.
Nice to have
• The new materials may be solely used in the north America and distributed in Australia as well. Therefore, we may try something new in these markets. I'd prefer to see a broader use of the color spectrum, not simply blue.
Should not have
• The card should not look and feel like a bank, insurance company, or a traditional money manager.

```html
<!DOCTYPE html>
<html lang="en">
<head>
<meta charset="utf-8">
<title>NorthmerrowCap Business Card</title>
<link href="https://fonts.googleapis.com/css2?family=Roboto:wght@300;400;500;700&display=swap" rel="stylesheet">
<style>
  :root {
    --paper: #ffffff;
    --aqua: #63f3ff;
    --navy: #0d2f6e;
    --ink: #222222;
    --white: #ffffff;
  }
  * { margin: 0; padding: 0; box-sizing: border-box; }
  html, body {
    width: 1050px;
    height: 1200px;
    overflow: hidden;
    background: var(--paper);
    font-family: "Roboto", "Helvetica Neue", Arial, sans-serif;
  }
  .card {
    position: relative;
    width: 1050px;
    height: 1200px;
  }
  .card-front {
    position: absolute;
    top: 0; left: 0;
    width: 1050px;
    height: 600px;
    background: var(--paper);
  }
  .brand {
    position: absolute;
    left: 203px;
    top: 251px;
    display: flex;
    align-items: center;
    gap: 26px;
  }
  .brand-mark {
    width: 88px;
    height: 88px;
    display: block;
  }
  .brand-name {
    font-size: 66px;
    font-weight: 500;
    color: var(--navy);
    letter-spacing: 0.5px;
    line-height: 1;
  }
  .card-back {
    position: absolute;
    top: 600px; left: 0;
    width: 1050px;
    height: 600px;
    background: var(--aqua);
    text-align: center;
  }
  .holder-name {
    position: absolute;
    left: 0; right: 0;
    top: 175px;
    font-size: 42px;
    font-weight: 700;
    color: var(--white);
    line-height: 1;
  }
  .holder-role {
    position: absolute;
    left: 0; right: 0;
    top: 226px;
    font-size: 33px;
    font-weight: 400;
    color: var(--ink);
    line-height: 1;
  }
  .contact {
    position: absolute;
    left: 0; right: 0;
    top: 306px;
    font-size: 33px;
    font-weight: 300;
    color: var(--white);
    line-height: 41px;
    list-style: none;
  }
</style>
</head>
<body>
  <main class="card">
    <section class="card-front">
      <div class="brand">
        <svg class="brand-mark" viewBox="0 0 88 88" aria-hidden="true">
          <circle cx="44" cy="44" r="44" fill="#0d2f6e"/>
        </svg>
        <span class="brand-name">NorthmerrowCap</span>
      </div>
    </section>
    <section class="card-back">
      <h1 class="holder-name">Henrik L. Dahl</h1>
      <p class="holder-role">Founder</p>
      <ul class="contact">
        <li class="contact-email">hdahl@northmerrowcap.com</li>
        <li class="contact-phone">(+01)5550142876</li>
      </ul>
    </section>
  </main>
</body>
</html>
```